MRHT Needs Fundraiser Dinner Invite!!

The Marisol Hendrick Trust, a 501 3(c) non for profit has a yearly fundraiser, with varying themes. Last year it was "cowboys" and "cowgirls"
This year, it is Club Orchid, or 70's disco music. I have uploaded last years invite for reference, some stock photography for inspiration. You are not limited to using the stock photos.

Annual MRHT Fundraiser Dinner
October 13th, 2022
Starts: 6:30pm
RSVP By: September 20th
Place: The Bramwell
Price: $135 per ticket

Target Market(s)

Donors, Business People, Every person

Industry/Entity Type

Non for Profit

Font styles to use
Sans Serif

Colors
0054AA
0677BA
7BADD7
CADEEF
E8F1F8
E54698
E96AAD
F1A4CE
F9D9EA
FCEFF6
6B429C
8869AF
B7A5CE
E3DAEB
F3F0F8

Requirements
Must have
• The invite should be 5x7, be sophisticated as the clientele are mainly business people that come to support the cause. It should be fun and inviting at the same time.

```html
<!DOCTYPE html>
<html lang="en">
<head>
<meta charset="utf-8">
<title>Annual MRHT Fundraiser Dinner</title>
<link rel="stylesheet" href="https://fonts.googleapis.com/css2?family=Montserrat:wght@300;600;700&family=Archivo+Black&family=Oswald:wght@300;400&family=Big+Shoulders+Display:wght@700&display=swap">
<style>
  :root {
    --magenta: #f224f0;
    --plum: #a1009f;
    --ink: #0d0d12;
    --white: #ffffff;
    --shadow-blue: #3c5aa8;
  }
  * { margin: 0; padding: 0; box-sizing: border-box; }
  html, body { width: 857px; height: 1200px; overflow: hidden; background: var(--white); }
  .invite { position: relative; width: 857px; height: 1200px; overflow: hidden; font-family: "Montserrat", sans-serif; }
  .scene { position: absolute; inset: 0; }
  .brand { position: absolute; left: 46px; top: 50px; display: flex; align-items: center; gap: 14px; }
  .brand-dot { width: 52px; height: 52px; border-radius: 50%; background: var(--white); }
  .brand-name { font-family: "Montserrat", sans-serif; font-weight: 700; font-size: 29px; color: var(--white); letter-spacing: 0.5px; white-space: nowrap; }
  .centered { position: absolute; left: 0; width: 857px; text-align: center; white-space: nowrap; }
  .eyebrow { top: 304px; font-weight: 600; font-size: 41px; line-height: 1.1; color: var(--magenta); letter-spacing: 1.5px; }
  .event-kind { top: 356px; font-weight: 300; font-size: 67px; line-height: 1.1; color: var(--white); letter-spacing: 2px; }
  .headline {
    top: 418px; font-family: "Big Shoulders Display", sans-serif; font-weight: 700; font-size: 212px; line-height: 1; letter-spacing: 4px;
    background: linear-gradient(to bottom, var(--white) 0 58%, var(--magenta) 58% 100%);
    -webkit-background-clip: text; background-clip: text; color: transparent;
    filter: drop-shadow(5px 5px 0 var(--shadow-blue));
  }
  .date-band { position: absolute; left: 0; top: 628px; width: 857px; height: 78px; background: var(--magenta); box-shadow: 0 6px 10px rgba(120,0,120,0.45); }
  .date { top: 628px; font-family: "Oswald", sans-serif; font-weight: 300; font-size: 54px; line-height: 78px; color: var(--white); letter-spacing: 3px; }
  .start { top: 742px; font-family: "Oswald", sans-serif; font-weight: 300; font-size: 40px; line-height: 54px; color: var(--ink); letter-spacing: 2px; }
  .rsvp { top: 815px; font-family: "Archivo Black", sans-serif; font-size: 36px; line-height: 44px; color: var(--magenta); }
  .venue { top: 870px; font-family: "Oswald", sans-serif; font-weight: 300; font-size: 52px; line-height: 70px; color: var(--ink); letter-spacing: 3px; }
  .price-ring { position: absolute; left: 596px; top: 880px; width: 410px; height: 410px; border-radius: 50%; background: rgba(220,225,245,0.55); }
  .price-disc { position: absolute; left: 617px; top: 902px; width: 380px; height: 380px; border-radius: 50%; background: var(--plum); }
  .ticket-icon { position: absolute; left: 737px; top: 928px; width: 60px; height: 62px; }
  .price-label { position: absolute; right: 17px; top: 1006px; font-family: "Oswald", sans-serif; font-weight: 400; font-size: 38px; line-height: 46px; color: var(--ink); letter-spacing: 2px; white-space: nowrap; text-align: right; }
  .price { position: absolute; right: 12px; top: 1050px; font-family: "Big Shoulders Display", sans-serif; font-weight: 700; font-size: 110px; line-height: 96px; color: var(--white); letter-spacing: 1px; white-space: nowrap; text-align: right; }
</style>
</head>
<body>
<main class="invite">
  <svg class="scene" width="857" height="1200" viewBox="0 0 857 1200" role="img" aria-label="Disco scene: glowing mirror ball above, bokeh lights, knife and fork, dancers in silhouette on a lit dance floor">
    <defs>
      <radialGradient id="glow" cx="0.5" cy="0.5" r="0.7">
        <stop offset="0" stop-color="#eef0fb"/>
        <stop offset="0.45" stop-color="#aab9f4"/>
        <stop offset="1" stop-color="#3c63ee"/>
      </radialGradient>
      <linearGradient id="ball" x1="0" y1="0" x2="1" y2="1">
        <stop offset="0" stop-color="#0c0a1c"/>
        <stop offset="0.6" stop-color="#4b2ab8"/>
        <stop offset="1" stop-color="#a38de8"/>
      </linearGradient>
      <linearGradient id="crowd" x1="0" y1="0" x2="1" y2="0">
        <stop offset="0" stop-color="#101218" stop-opacity="0.9"/>
        <stop offset="1" stop-color="#101218" stop-opacity="0"/>
      </linearGradient>
    </defs>
    <rect width="857" height="1200" fill="url(#glow)"/>
    <ellipse cx="430" cy="120" rx="470" ry="350" fill="url(#ball)"/>
    <rect x="0" y="720" width="300" height="480" fill="url(#crowd)"/>
  </svg>

  <div class="brand">
    <span class="brand-dot"></span>
    <span class="brand-name">MRHT.ORG</span>
  </div>

  <p class="centered eyebrow">ANNUAL MRHT</p>
  <p class="centered event-kind">FUNDRAISER</p>
  <h1 class="centered headline">DINNER</h1>

  <div class="date-band"></div>
  <p class="centered date">OCTOBER 13TH, 2022</p>

  <p class="centered start">STARTS: 6:30PM</p>
  <p class="centered rsvp">RSVP BY: SEPTEMBER 20TH</p>
  <p class="centered venue">THE BRAMWELL</p>

  <div class="price-ring"></div>
  <div class="price-disc"></div>
  <svg class="ticket-icon" viewBox="0 0 60 62" aria-hidden="true">
    <path d="M14 12 L40 4 L56 40 L30 56 Q24 50 18 52 L6 30 Q12 24 8 18 Z" fill="none" stroke="#ffffff" stroke-width="5" stroke-linejoin="round"/>
    <circle cx="26" cy="30" r="2.5" fill="#ffffff"/>
    <circle cx="34" cy="26" r="2.5" fill="#ffffff"/>
    <circle cx="32" cy="38" r="2.5" fill="#ffffff"/>
  </svg>
  <p class="price-label">PER TICKET</p>
  <p class="price">$135</p>
</main>
</body>
</html>
```